Logo and bag for Turkish coffee brand

We are a coffee roasting company. We need a logo for our new Turkish coffee brand. We are targeting C+ to A- customer segment. Our brand is above average in pricing and can be expressed as very good in quality or a bit less than excellentOur brand name is قهواكQahwakIt is an Arabic word that means "Your coffee" and if read in a different way it means "I love You"

Target Market(s)

We are selling in Egyptian market for customer segments from C+ and up to A-

Logo Text

Binnitak بنّيتك

Requirements
Must have
• 1. The logo must contain brand name in Arabic good to have it in Arabic and English if possible.
• 2. All text content must be in Arabic and good to be in both Arabic and English
• 3. The package must include two spaces for limited text paragraphs
• an area for production date and expiry.
• 4. An area for selecting variants of the product. Our coffee has light-medium-dark roasted (فاتح - وسط - غامق)
• Plain or flavored (سادة - محوج)

```html
<!DOCTYPE html>
<html lang="en">
<head>
<meta charset="utf-8">
<title>Binnitak Turkish Coffee – Bag Fronts</title>
<link rel="stylesheet" href="https://fonts.googleapis.com/css2?family=Cairo:wght@400;700&family=Raleway:wght@400&display=swap">
<style>
  :root {
    --canvas-bg: #efeff0;
    --light-bag: #bad9d7;
    --dark-bag: #27254b;
    --gold: #d6a358;
    --bean-brown: #5a2d16;
    --light-title: #2f6192;
    --dark-title: #c3cbe0;
    --light-ink: #2b2f45;
    --dark-ink: #e9e9f2;
    --light-rule: #7f9aa6;
    --dark-rule: #8a89a8;
    --rosette-teal: #3bb3c3;
    --rosette-blue: #2360a0;
    --rosette-gold: #e2a94c;
    --rosette-green: #27a36f;
    --rosette-rust: #b95a2a;
  }
  * { box-sizing: border-box; margin: 0; padding: 0; }
  html, body {
    width: 1200px; height: 1000px; overflow: hidden;
    background: var(--canvas-bg);
  }
  .canvas { position: relative; width: 1200px; height: 1000px; }

  .bag {
    position: absolute;
    top: 82px;
    height: 885px;
    overflow: hidden;
  }
  .bag--light { left: 60px; width: 555px; background: var(--light-bag); }
  .bag--dark  { left: 632px; width: 543px; background: var(--dark-bag); }

  .brand-mark {
    position: absolute;
    top: 95px; left: 0; right: 0;
    display: flex; align-items: center; justify-content: center; gap: 16px;
    font-family: 'Cairo', sans-serif;
    font-weight: 700;
    color: var(--gold);
  }
  .brand-mark__dot {
    width: 34px; height: 34px; border-radius: 50%;
    background: var(--bean-brown);
  }
  .brand-mark__names { display: flex; flex-direction: column; align-items: center; line-height: 1; }
  .brand-mark__arabic { font-size: 92px; line-height: 1.1; }
  .brand-mark__latin { font-size: 24px; letter-spacing: 1px; }

  .product-title {
    position: absolute;
    top: 255px; left: 0; right: 0;
    text-align: center;
    font-family: 'Raleway', sans-serif;
    font-weight: 400;
    font-size: 25px;
    letter-spacing: 0.5px;
  }
  .bag--light .product-title { color: var(--light-title); }
  .bag--dark .product-title { color: var(--dark-title); }

  .variant-panel {
    position: absolute;
    top: 598px;
    width: 122px;
    font-family: 'Cairo', sans-serif;
    text-align: right;
  }
  .bag--light .variant-panel { left: 78px; color: var(--light-ink); }
  .bag--dark .variant-panel { left: 76px; color: var(--dark-ink); }
  .variant-panel__name { font-size: 21px; font-weight: 700; line-height: 1.3; margin-right: -42px; }
  .variant-panel__rule { height: 1px; width: 122px; margin: 36px 0 22px; }
  .bag--light .variant-panel__rule { background: var(--light-rule); }
  .bag--dark .variant-panel__rule { background: var(--dark-rule); }
  .variant-panel__option { font-size: 15px; line-height: 1.75; margin-right: -2px; }
  .variant-panel__option { text-align: left; }

  .rosette-cluster {
    position: absolute;
    right: 0; bottom: 0;
    border-top-left-radius: 120px 260px;
    background: linear-gradient(160deg,
      var(--rosette-gold) 0%,
      var(--rosette-teal) 30%,
      var(--rosette-blue) 55%,
      var(--rosette-green) 78%,
      var(--rosette-rust) 100%);
    opacity: 0.85;
  }
  .bag--light .rosette-cluster { width: 300px; height: 420px; }
  .bag--dark .rosette-cluster { width: 300px; height: 440px; }
</style>
</head>
<body>
<main class="canvas">

  <section class="bag bag--light" aria-label="Light roast bag front">
    <div class="brand-mark">
      <span class="brand-mark__dot"></span>
      <div class="brand-mark__names">
        <span class="brand-mark__latin">Binnitak</span>
        <span class="brand-mark__arabic" lang="ar">بنّيتك</span>
      </div>
    </div>
    <p class="product-title">-TURKISH COFFEE-</p>
    <div class="variant-panel" lang="ar" dir="rtl">
      <p class="variant-panel__name">قهوة تركية</p>
      <div class="variant-panel__rule"></div>
      <p class="variant-panel__option">فاتح</p>
      <p class="variant-panel__option">سادة</p>
    </div>
    <div class="rosette-cluster" role="img" aria-label="Cluster of multicoloured geometric star rosettes in teal, blue, gold, green and rust"></div>
  </section>

  <section class="bag bag--dark" aria-label="Dark roast bag front">
    <div class="brand-mark">
      <span class="brand-mark__dot"></span>
      <div class="brand-mark__names">
        <span class="brand-mark__latin">Binnitak</span>
        <span class="brand-mark__arabic" lang="ar">بنّيتك</span>
      </div>
    </div>
    <p class="product-title">-TURKISH COFFEE-</p>
    <div class="variant-panel" lang="ar" dir="rtl">
      <p class="variant-panel__name">قهوة تركية</p>
      <div class="variant-panel__rule"></div>
      <p class="variant-panel__option">غامق</p>
      <p class="variant-panel__option">سادة</p>
    </div>
    <div class="rosette-cluster" role="img" aria-label="Cluster of multicoloured geometric star rosettes in teal, blue, gold, green and rust"></div>
  </section>

</main>
</body>
</html>
```